Business Card Design

Just looking for a good designs that looks good with our company logo. I'd like it to be simple and to the point. Just including contact information, our logo, and my name somewhere on the card so future clients know who they're contacting, and a couple services offered. The two images I attached are pictures of our logo. I don't care which color they they are, I just attached both images to give a reference of logo colors depending on the color of the card.
Names: Derek Hallory
Phone: 816-442-7061
Email: greenvalebrush@mailzen.test
Services offered:
Mowing
Fertilization
Aeration
Bed & tree maintenance
and more.
Industry/Entity Type
Business
Contact Information for Business Card
Names: Derek Hallory
Phone: 816-442-7061
Look and feel

```html
<!DOCTYPE html>
<html lang="en">
<head>
<meta charset="utf-8">
<title>Greenvale Brush — Business Card</title>
<link rel="stylesheet" href="https://fonts.googleapis.com/css2?family=Open+Sans:ital,wght@0,400;0,700;1,400&display=swap">
<style>
  :root {
    --page: #ecece8;
    --card: #ffffff;
    --grass-light: #5fb83c;
    --grass-mid: #3f9a28;
    --grass-dark: #2c7a1c;
    --ink: #2a2a32;
    --logo-text: #ffffff;
  }
  * { box-sizing: border-box; margin: 0; padding: 0; }
  html, body { width: 1200px; height: 1000px; overflow: hidden; }
  body {
    background: var(--page);
    font-family: "Open Sans", Arial, sans-serif;
    color: var(--ink);
    display: flex;
    flex-direction: column;
    align-items: center;
    justify-content: center;
    gap: 40px;
  }
  .card {
    position: relative;
    width: 770px;
    height: 440px;
    background: var(--card);
    overflow: hidden;
    box-shadow: 0 6px 18px rgba(0,0,0,0.18);
  }
  .grass {
    position: absolute;
    top: 0;
    height: 100%;
    background:
      radial-gradient(circle at 40% 40%, var(--grass-light) 0%, var(--grass-mid) 55%, var(--grass-dark) 100%);
    border-radius: 0 50% 50% 0 / 0 50% 50% 0;
    box-shadow: 8px 0 14px rgba(0,0,0,0.35);
  }
  .card-front .grass { left: 0; width: 88%; }
  .card-back .grass { left: -240px; width: 500px; }

  .brand {
    position: absolute;
    left: 44%;
    top: 50%;
    transform: translate(-50%, -50%);
    display: flex;
    align-items: center;
    gap: 18px;
  }
  .brand-dot {
    width: 34px; height: 34px;
    border-radius: 50%;
    background: var(--logo-text);
  }
  .brand-name {
    font-size: 58px;
    font-weight: 700;
    color: var(--logo-text);
    letter-spacing: 2px;
    white-space: nowrap;
  }

  .contact {
    position: absolute;
    right: 52px;
    top: 58px;
    text-align: right;
  }
  .contact-name {
    font-size: 42px;
    font-weight: 400;
    margin-bottom: 50px;
  }
  .contact-line {
    font-size: 27px;
    line-height: 1.3;
  }
  .services {
    margin-top: 42px;
    font-size: 17px;
    font-style: italic;
    line-height: 2;
  }
</style>
</head>
<body>
  <section class="card card-front" aria-label="Card front">
    <div class="grass" role="img" aria-label="Close-up photo of green lawn grass"></div>
    <div class="brand">
      <span class="brand-dot"></span>
      <span class="brand-name">GREENVALE BRUSH</span>
    </div>
  </section>

  <section class="card card-back" aria-label="Card back">
    <div class="grass" role="img" aria-label="Close-up photo of green lawn grass"></div>
    <div class="contact">
      <p class="contact-name">Derek Hallory</p>
      <p class="contact-line">Phone: 816-442-7061</p>
      <p class="contact-line">Email: greenvalebrush@mailzen.test</p>
      <div class="services">
        <p>Mowing, Fertilization, Aeration</p>
        <p>Bed &amp; tree maintenance and more.</p>
      </div>
    </div>
  </section>
</body>
</html>
```